The Velvet Magpie business card

I need a business card for my makeup artist business. I specialise in bridal, glamour, formal and special occasion makeup.
I am a mobile makeup artist who caters for every from nowra to sydney.
I do the following services:
Bridal makeup
airbrush makeup
special occasion
formals
hens nights/ girls night
makeup lesson
makeup for all ages from flower girl to Nanna of the bride!
photoshoot makeup
SPFX

I would like the card to portray a very professional sleek makeup business. I would also like another version of the card directed especially towards brides.

Please see my website to understand colours etc www.thevelvetmagpie.com

Industry/Entity Type

Business

Contact Information for Business Card

The Velvet Magpie
Professional Makeup Artist
Marguerite Olvey
0412083946
info@thevelvetmagpie.com
www.thevelvetmagpie.com
www.friendsnook.com/thevelvetmagpie

```html
<!DOCTYPE html>
<html lang="en">
<head>
<meta charset="utf-8">
<title>The Velvet Magpie – Business Card</title>
<link rel="stylesheet" href="https://fonts.googleapis.com/css2?family=Lobster&family=Crimson+Text:wght@400&family=Lobster+Two:wght@700&display=swap">
<style>
  :root {
    --bg: #cfd1d3;
    --card-black: #0b0a0a;
    --pink: #e4147f;
    --white: #ffffff;
    --photo-dark: #2a2220;
    --photo-warm: #a77a60;
    --photo-light: #d9b79a;
  }
  * { box-sizing: border-box; margin: 0; padding: 0; }
  html, body { width: 1200px; height: 1038px; overflow: hidden; }
  body {
    background: var(--bg);
    display: flex;
    align-items: center;
    justify-content: center;
    gap: 90px;
  }
  .card {
    position: relative;
    width: 400px;
    height: 700px;
    background: var(--card-black);
    overflow: hidden;
    box-shadow: 0 6px 18px rgba(0,0,0,0.25);
  }

  /* Front */
  .front__header {
    position: absolute; top: 0; left: 0; right: 0;
    height: 110px;
    border-bottom: 3px solid var(--pink);
    text-align: center;
    padding-top: 22px;
  }
  .brand-name {
    font-family: "Lobster", cursive;
    color: var(--pink);
    font-size: 30px;
    line-height: 1.1;
  }
  .brand-role {
    font-family: "Crimson Text", serif;
    color: var(--pink);
    font-size: 21px;
    letter-spacing: 0.5px;
  }
  .front__photo {
    position: absolute; top: 113px; left: 0; right: 0;
    height: 380px;
    background: radial-gradient(ellipse at 45% 45%, var(--photo-light) 0%, var(--photo-warm) 35%, var(--photo-dark) 70%, var(--card-black) 100%);
  }
  .front__details {
    position: absolute; left: 28px; bottom: 26px; right: 20px;
  }
  .person-name {
    font-family: "Lobster", cursive;
    color: var(--pink);
    font-size: 30px;
    margin-bottom: 8px;
  }
  .contact-list { list-style: none; }
  .contact-list li {
    display: flex; align-items: center; gap: 10px;
    font-family: "Crimson Text", serif;
    color: var(--white);
    font-size: 20px;
    line-height: 34px;
    white-space: nowrap;
  }
  .contact-list svg { width: 18px; height: 18px; flex: none; }

  /* Back */
  .back__photo {
    position: absolute; inset: 0;
    background: radial-gradient(ellipse at 55% 30%, var(--photo-light) 0%, var(--photo-warm) 30%, var(--photo-dark) 65%, var(--card-black) 100%);
  }
  .back__seal {
    position: absolute; left: 50%; bottom: -150px;
    width: 360px; height: 360px;
    transform: translateX(-50%);
    border-radius: 50%;
    background: var(--card-black);
    border: 4px solid var(--white);
    box-shadow: 0 0 0 10px var(--card-black), 0 0 0 12px var(--white);
  }
  .back__text {
    position: absolute; left: 0; right: 0; bottom: 48px;
    text-align: center;
  }
  .book-line {
    font-family: "Lobster Two", cursive;
    font-weight: 700;
    color: var(--white);
    font-size: 21px;
    margin-top: 10px;
  }
</style>
</head>
<body>

  <section class="card card--front">
    <header class="front__header">
      <div class="brand-name">The Velvet Magpie</div>
      <div class="brand-role">Professional Makeup Artist</div>
    </header>
    <div class="front__photo" role="img" aria-label="Close-up portrait photograph of a model wearing dramatic blue eye makeup and dark lipstick"></div>
    <div class="front__details">
      <div class="person-name">Marguerite Olvey</div>
      <ul class="contact-list">
        <li>
          <svg viewBox="0 0 18 18"><circle cx="9" cy="9" r="9" fill="#fff"/><path d="M6 4.5l2 2-1 1.2c.6 1.3 1.6 2.3 2.9 2.9l1.2-1 2 2-1.2 1.4c-3.4-.4-6.4-3.4-6.8-6.8z" fill="#0b0a0a"/></svg>
          0412083946
        </li>
        <li>
          <svg viewBox="0 0 18 18"><rect x="1" y="4" width="16" height="11" fill="#fff"/><path d="M1 4l8 6 8-6" fill="none" stroke="#0b0a0a" stroke-width="1.3"/></svg>
          info@thevelvetmagpie.com
        </li>
        <li>
          <svg viewBox="0 0 18 18"><circle cx="9" cy="9" r="8" fill="#fff"/><g fill="none" stroke="#0b0a0a" stroke-width="1"><ellipse cx="9" cy="9" rx="3.5" ry="8"/><path d="M1 9h16M2.5 5h13M2.5 13h13"/></g></svg>
          www.thevelvetmagpie.com
        </li>
        <li>
          <svg viewBox="0 0 18 18"><rect x="1" y="1" width="16" height="16" fill="#fff"/></svg>
          www.friendsnook.com/thevelvetmagpie
        </li>
      </ul>
    </div>
  </section>

  <section class="card card--back">
    <div class="back__photo" role="img" aria-label="Photograph of a model with tousled blonde hair in a black top, hands raised in her hair"></div>
    <div class="back__seal"></div>
    <div class="back__text">
      <div class="brand-name">The Velvet Magpie</div>
      <div class="brand-role">Professional Makeup Artist</div>
      <div class="book-line">Call 0412 083 946 To Book</div>
    </div>
  </section>

</body>
</html>
```